Wren's Hearth Support Business Card

Business card design
Font must be in Poppins Regular for Wren's Hearth Support
Safe Days Ahead font is Alex Brush

Colour must be Hex #910E2B
RGB 145-14-43
Pantone 7427 C
We want the card editable
On the front please include
Name eg Mavis Dunleavy
Position eg Clinical Care Manager
Phone number mobile 0473 856 342
Phone 08 7394 2650
Email : mavis@wrenshearthsupport.com.au
Address : Gullwing Cove, Western Australia, 6258
Website : wrenshearthsupport.com.au
Contact us today to experience the warmth, respect and personal touch of Wren's Hearth Support.

Target Market(s)

35+

Industry/Entity Type

aged care / community

Contact Information for Business Card

see project description

Requirements
Must have
• Colours, logos and fonts as detailed and uploaded

```html
<!DOCTYPE html>
<html lang="en">
<head>
<meta charset="utf-8">
<title>Wren's Hearth Support – Business Card</title>
<link rel="stylesheet" href="https://fonts.googleapis.com/css2?family=Poppins:wght@400;600&family=Alex+Brush&display=swap">
<style>
  :root {
    --brand-red: #910e2b;
    --card-ink: #222226;
    --text-light: #f2f2f2;
    --backdrop: #d3d8d8;
  }
  * { margin: 0; padding: 0; box-sizing: border-box; }
  html, body { width: 1200px; height: 960px; overflow: hidden; }
  body {
    background: radial-gradient(ellipse at center, #dde1e1 0%, var(--backdrop) 70%, #c9cfcf 100%);
    font-family: "Poppins", sans-serif;
    position: relative;
  }
  .card {
    position: absolute;
    left: 250px;
    width: 701px;
    height: 401px;
    background: var(--card-ink);
    border-left: 8px solid var(--brand-red);
    border-right: 8px solid var(--brand-red);
    box-shadow: 0 10px 22px rgba(0, 0, 0, 0.35);
  }
  .card--front { top: 60px; }
  .card--back { top: 500px; }

  .lockup { position: absolute; color: var(--brand-red); }
  .lockup__ring {
    position: absolute;
    border: 8px solid var(--brand-red);
    border-radius: 50%;
  }
  .lockup__name {
    position: absolute;
    font-weight: 400;
    line-height: 1.1;
    white-space: nowrap;
  }
  .lockup__tagline {
    position: absolute;
    font-family: "Alex Brush", cursive;
    white-space: nowrap;
  }

  /* front */
  .card--front .lockup__ring { left: 92px; top: 129px; width: 140px; height: 140px; }
  .card--front .lockup__name { left: 242px; top: 116px; font-size: 46px; }
  .card--front .lockup__tagline { left: 244px; top: 226px; font-size: 38px; }
  .invitation {
    position: absolute;
    left: 0; right: 0; top: 329px;
    text-align: center;
    color: var(--text-light);
    font-size: 16px;
    line-height: 24px;
    letter-spacing: 0.4px;
  }

  /* back */
  .name-marker {
    position: absolute;
    left: 0; top: 32px;
    width: 13px; height: 44px;
    background: var(--brand-red);
  }
  .person {
    position: absolute;
    left: 19px; top: 24px;
  }
  .person__name {
    color: var(--brand-red);
    font-size: 33px;
    line-height: 38px;
    font-weight: 400;
  }
  .person__name strong { font-weight: 600; }
  .person__role {
    color: var(--text-light);
    font-size: 17px;
    line-height: 20px;
  }
  .address {
    position: absolute;
    left: 19px; top: 203px;
    color: var(--brand-red);
    font-size: 16px;
    line-height: 24px;
    letter-spacing: 0.5px;
  }
  .contacts {
    position: absolute;
    left: 19px; top: 281px;
    list-style: none;
  }
  .contacts li {
    display: flex;
    align-items: center;
    height: 23.5px;
    color: var(--text-light);
    font-size: 16.5px;
    letter-spacing: 0.3px;
  }
  .contacts svg { width: 16px; height: 16px; margin-right: 15px; flex: none; }
  .card--back .lockup__ring { left: 349px; top: 151px; width: 104px; height: 104px; border-width: 6px; }
  .card--back .lockup__name { left: 456px; top: 143px; font-size: 28px; }
  .card--back .lockup__tagline { left: 457px; top: 207px; font-size: 27px; }
</style>
</head>
<body>

<section class="card card--front">
  <div class="lockup">
    <span class="lockup__ring"></span>
    <p class="lockup__name">Wren's<br>Hearth Support</p>
    <p class="lockup__tagline">Safe Days Ahead</p>
  </div>
  <p class="invitation">Contact us today to experience the warmth,<br>respect and personal touch of Wren's Hearth Support</p>
</section>

<section class="card card--back">
  <span class="name-marker"></span>
  <div class="person">
    <h1 class="person__name"><strong>Mavis</strong> Dunleavy</h1>
    <p class="person__role">Clinical Care Manager</p>
  </div>

  <p class="address">Gullwing Cove,<br>Western Australia, 6258</p>

  <ul class="contacts">
    <li>
      <svg viewBox="0 0 16 16" aria-hidden="true"><rect x="4" y="1" width="8" height="14" rx="1.5" fill="none" stroke="#910e2b" stroke-width="1.6"/><circle cx="8" cy="9" r="1.4" fill="#910e2b"/></svg>
      0473 856 342
    </li>
    <li>
      <svg viewBox="0 0 16 16" aria-hidden="true"><path d="M3 2l3 0 1 3.5-2 1.3a9 9 0 0 0 4.2 4.2l1.3-2 3.5 1v3a1.5 1.5 0 0 1-1.6 1.5A12.5 12.5 0 0 1 1.5 3.6 1.5 1.5 0 0 1 3 2z" fill="#910e2b"/></svg>
      08 7394 2650
    </li>
    <li>
      <svg viewBox="0 0 16 16" aria-hidden="true"><circle cx="8" cy="8" r="6.5" fill="none" stroke="#910e2b" stroke-width="1.5"/><ellipse cx="8" cy="8" rx="2.8" ry="6.5" fill="none" stroke="#910e2b" stroke-width="1.2"/><path d="M1.5 8h13" stroke="#910e2b" stroke-width="1.2"/></svg>
      www.wrenshearthsupport.com.au
    </li>
    <li>
      <svg viewBox="0 0 16 16" aria-hidden="true"><rect x="1.5" y="4" width="13" height="9.5" rx="1" fill="none" stroke="#910e2b" stroke-width="1.5"/><path d="M1.8 4.5L8 9.5l6.2-5" fill="none" stroke="#910e2b" stroke-width="1.5"/></svg>
      mavis@wrenshearthsupport.com.au
    </li>
  </ul>

  <div class="lockup">
    <span class="lockup__ring"></span>
    <p class="lockup__name">Wren's<br>Hearth Support</p>
    <p class="lockup__tagline">Safe Days Ahead</p>
  </div>
</section>

</body>
</html>
```